Service Menu refresh 2018 Update of menu pricing

We currently have service menus as attached. We will be updating our look via our homepage image, our service menu and our in-house beverage and treatment menu.
We are a natural and sustainable hair salon group and moving more towards head spa which consists of treatments, beauty, tanning as well as your traditional hair services. Our imagery needs to reflect our efforts in spa treatments in the hair and scalp area and use natural materials and colours reflecting sustainability.
Velin is the brand we stock and promote.

Target Market(s)

Men or women interesting in personal maintenance with natural and organic products and using sustainable practises

Industry/Entity Type

Hair And Beauty

Font styles to use
Sans Serif
Other font styles liked:
• Arial or Helvetica

Colors
9acb3c
abd037
cadf82
ffffff

Requirements
Must have
• Name on the front cover, locations on back cover
Nice to have
• Prestige feel, reflect male and female clients
Should not have
• Bold artificial writing or any type of cartoon images.
• Same images as existing menu.

```html
<!DOCTYPE html>
<html lang="en">
<head>
<meta charset="utf-8">
<title>Verdant Roots Hair Studios – Menu Cover</title>
<link href="https://fonts.googleapis.com/css2?family=Lato:wght@400;700&family=Kalam:wght@300&display=swap" rel="stylesheet">
<style>
  :root{
    --stage:#d9d9d9;
    --ink:#231f20;
    --ink-soft:#2e2a2b;
    --leaf:#8cc63f;
    --leaf-bright:#9acb3c;
    --leaf-deep:#5e9e2a;
    --leaf-pale:#cadf82;
    --white:#ffffff;
    --hair-dark:#5a2a14;
    --hair-warm:#a1522a;
  }
  *{box-sizing:border-box;margin:0;padding:0}
  html,body{width:1200px;height:1200px;overflow:hidden}
  body{background:var(--stage);display:flex;align-items:center;justify-content:center;font-family:"Lato",Arial,sans-serif}
  .spread{width:1080px;height:764px;display:flex;box-shadow:0 10px 30px rgba(0,0,0,.25)}
  .back-cover{width:540px;height:100%;position:relative;text-align:center;color:var(--white);
    background:linear-gradient(180deg,var(--ink) 0%,var(--ink) 55%,var(--ink-soft) 100%)}
  .front-cover{width:540px;height:100%;position:relative;overflow:hidden;
    background:linear-gradient(160deg,var(--leaf-bright) 0%,var(--leaf) 50%,var(--leaf-deep) 100%)}
  .brand{display:flex;align-items:center;gap:12px;font-weight:400;letter-spacing:.3px}
  .brand-dot{width:34px;height:34px;border-radius:50%;background:var(--leaf-bright);flex:none}
  .back-cover .brand{position:absolute;top:50px;left:0;right:0;justify-content:center;font-size:30px;color:var(--white)}
  .front-cover .brand{position:absolute;top:72px;left:30px;font-size:36px;color:var(--white)}
  .front-cover .brand-dot{background:var(--white);width:40px;height:40px}
  .tagline{position:absolute;top:138px;left:30px;right:20px;font-family:"Kalam",cursive;font-weight:300;
    color:var(--leaf-bright);font-size:17px;line-height:21px}
  .location{position:absolute;left:20px;right:20px}
  .location.first{top:234px}
  .location.second{top:394px}
  .location h2{font-weight:400;font-size:26px;letter-spacing:.5px;margin-bottom:12px}
  .row{display:flex;justify-content:center;align-items:center;gap:8px;font-size:17px;line-height:21px}
  .row svg{flex:none}
  .address{margin-bottom:12px}
  .phone{font-size:27px;color:var(--leaf-bright);margin-bottom:14px}
  .email{font-size:17px}
  .photo-frame{position:absolute;inset:0}
</style>
</head>
<body>
<main class="spread">
  <section class="back-cover">
    <div class="brand"><span class="brand-dot"></span>Verdant Roots Hair Studios</div>
    <p class="tagline">To fill a gap. Where stylists and clients want to make a difference, with a choice to be greener, together we can create a better option.</p>

    <div class="location first">
      <h2>BROOKVALE</h2>
      <p class="row address">
        <svg width="16" height="15" viewBox="0 0 16 15"><path d="M1 7 8 1l7 6M3 6v8h10V6M6 14V9h4v5" fill="none" stroke="var(--leaf-bright)" stroke-width="1.5"/></svg>
        Shop 1018 Linden Plaza Brookvale, Mill Rd, Brookvale
      </p>
      <p class="row phone">
        <svg width="22" height="24" viewBox="0 0 22 24"><rect width="22" height="24" rx="3" fill="var(--leaf-bright)"/><path d="M8 5c-2 1-3 3-2 7s4 7 7 7l2-2-3-3-2 1c-1-1-2-3-2-5l2-1-1-4z" fill="var(--ink)"/></svg>
        +61 (07) 3100 4521
      </p>
      <p class="row email">
        <svg width="20" height="13" viewBox="0 0 20 13"><rect width="20" height="13" fill="var(--leaf-bright)"/><path d="M0 0l10 7 10-7" fill="none" stroke="var(--ink)" stroke-width="1.5"/></svg>
        brookvale@verdantroots.example
      </p>
    </div>

    <div class="location second">
      <h2>ASHGROVE</h2>
      <p class="row address">
        <svg width="16" height="15" viewBox="0 0 16 15"><path d="M1 7 8 1l7 6M3 6v8h10V6M6 14V9h4v5" fill="none" stroke="var(--leaf-bright)" stroke-width="1.5"/></svg>
        <span>Shop 231 Linden Plaza Ashgrove, Hartley<br>Road, Ashgrove</span>
      </p>
      <p class="row phone">
        <svg width="22" height="24" viewBox="0 0 22 24"><rect width="22" height="24" rx="3" fill="var(--leaf-bright)"/><path d="M8 5c-2 1-3 3-2 7s4 7 7 7l2-2-3-3-2 1c-1-1-2-3-2-5l2-1-1-4z" fill="var(--ink)"/></svg>
        +61 (07) 3100 8834
      </p>
      <p class="row email">
        <svg width="20" height="13" viewBox="0 0 20 13"><rect width="20" height="13" fill="var(--leaf-bright)"/><path d="M0 0l10 7 10-7" fill="none" stroke="var(--ink)" stroke-width="1.5"/></svg>
        ashgrove@verdantroots.example
      </p>
    </div>
  </section>

  <section class="front-cover">
    <div class="brand"><span class="brand-dot"></span>Verdant Roots</div>
    <svg class="photo-frame" width="540" height="764" viewBox="0 0 540 764">
      <defs>
        <radialGradient id="hair-photo" cx="0.62" cy="0.62" r="0.6">
          <stop offset="0" stop-color="var(--hair-warm)"/>
          <stop offset="0.55" stop-color="var(--hair-dark)"/>
          <stop offset="1" stop-color="var(--white)"/>
        </radialGradient>
      </defs>
      <path d="M0 764C10 480 250 300 540 300V520C470 640 390 720 300 764Z" fill="var(--leaf-deep)"/>
      <path d="M0 764C10 490 250 312 540 312V500C460 620 370 710 270 764Z" fill="var(--white)"/>
      <path d="M20 764C40 520 260 340 530 322V500C450 620 360 710 260 764Z" fill="url(#hair-photo)"
            role="img" aria-label="Photo of a woman lying down with long curly auburn hair spread out, scattered with yellow petals"/>
    </svg>
  </section>
</main>
</body>
</html>
```